Car rental website design for a UAE car rental company

This project is about creating a new website design for a car rental company located in Dubai (United Arab Emirates), I opened the same project a few months ago but I didn't receive a lot of appealing entries so I closed it but this time I am marking the project as guaranteed to avoid such situation again, if you have already provided a design before then please re-submit again on this project so that it is considered while reviewing all the designs

A few important things:

1- We need a simple non-complex design
2- The final deliverable would be 2 screens (PSD, JPEG ... etc), the first screen is for the home page and the second screen is for an internal page
3- The home page must have a section that end users can use to rent a car online directly from the home page instead of going into some inner pages
4- The current website is very old and not very appealing so avoid creating a similar design (www.runo-vexa.example)
5- The name is Runovexa but the company rents normal cars (no Limousin cars will be rented) so avoid adding any fancy cars in the images/graphics used in the design, just normal end users cars
6- The expected pages would be: home, About us, Our team, Strategy, Contact us and links to social media pages
7- The attachments include the company's logo and some screens from other car rental companies that provide online rentals/payments

If you have any questions please feel free to ask and please note that we will need the designs urgently

Thanks

Target Market(s)

Dubai - United Arab Emirates

Industry/Entity Type

It Company

Number of Pages Required

2 page

Font styles to use
Sans Serif

Requirements
Must have
• Check the project details
Nice to have
Should not have

```html
<!DOCTYPE html>
<html lang="en">
<head>
<meta charset="utf-8">
<title>Runovexa Rent A Car</title>
<link href="https://fonts.googleapis.com/css2?family=Open+Sans:ital,wght@0,400;0,600;0,700;1,400&display=swap" rel="stylesheet">
<style>
:root{
  --ink:#222;
  --dark:#1f1f1f;
  --accent:#a5123d;
  --orange:#e2572b;
  --muted:#9a9a9a;
  --line:#d6d6d6;
  --field:#fff;
  --logos:#f3f3f3;
}
*{box-sizing:border-box;margin:0;padding:0}
html,body{width:674px;height:1200px;overflow:hidden;background:#fff}
body{font-family:"Open Sans",Arial,sans-serif;color:var(--ink);position:relative}
.abs{position:absolute}
.header{left:0;top:0;width:674px;height:50px;background:var(--dark)}
.header-rule{left:0;top:50px;width:674px;height:3px;background:#e9e9e9}
.brand{left:62px;top:0;width:141px;height:116px;background:#fff;z-index:3;display:flex;flex-direction:column;align-items:center;justify-content:center;gap:6px}
.brand-mark{width:40px;height:40px;border:3px solid var(--accent)}
.brand-name{font-size:19px;font-weight:700;color:var(--accent);letter-spacing:.5px}
.nav{left:284px;top:0;height:50px;display:flex;font-size:7px;text-transform:uppercase}
.nav a,.nav a:visited{color:#fff;text-decoration:none;padding:0 10px;line-height:54px}
.nav a.active{background:var(--accent);font-size:8px;width:43px}
.hero{left:0;top:53px;width:674px;height:313px;
  background:
    radial-gradient(ellipse 230px 95px at 480px 195px,rgba(12,12,14,.95),rgba(20,20,22,.7) 55%,rgba(20,20,22,0) 100%),
    radial-gradient(ellipse 120px 50px at 600px 230px,rgba(30,30,32,.8),rgba(30,30,32,0)),
    linear-gradient(180deg,#9fa1a3 0%,#b9bbbc 30%,#808284 55%,#3e3f41 80%,#2b2c2e 100%)}
.hero-title{left:64px;top:246px;width:306px;height:48px;background:#000;color:#fff;font-size:20px;font-weight:400;line-height:48px;padding-left:34px;font-family:Arial,sans-serif}
.hero-sub{left:75px;top:293px;width:300px;color:#fff;font-size:9px;font-weight:700;line-height:16px;text-transform:uppercase}
.hero-arrow{top:333px;width:18px;height:18px;border:1px solid #ddd;background:rgba(0,0,0,.3)}
.sec-title{left:0;width:674px;text-align:center;font-weight:700;font-size:17px;color:#333;text-transform:uppercase}
.sec-rule{left:263px;width:148px;height:1px;background:var(--line)}
.sec-rule::after{content:"";position:absolute;left:64px;top:-1px;width:20px;height:2px;background:var(--orange)}
.service{top:432px;width:130px;text-align:center}
.service svg{display:block;margin:0 auto;width:34px;height:34px}
.service .icon-base{width:40px;height:1px;background:var(--line);margin:2px auto 0}
.service h3{font-size:8px;font-weight:400;margin-top:10px;text-transform:uppercase;color:#333}
.service p{font-size:6px;color:var(--muted);line-height:12px;margin-top:7px}
.testimonials{left:0;top:553px;width:674px;height:215px;background:radial-gradient(ellipse at 30% 50%,#3b3b3b,#1c1c1c 70%)}
.t-title{color:#fff}
.t-sub{left:0;top:606px;width:674px;text-align:center;color:#fff;font-size:7px}
.t-card{top:638px;width:251px;height:91px;border:1px solid #666}
.t-photo{top:10px;width:48px;height:48px;border-radius:50%;border:3px solid #fff;background:linear-gradient(#c9b8a8,#8d7a6c)}
.t-name{top:12px;font-size:6.5px;color:#fff;text-transform:uppercase}
.t-line{top:26px;width:182px;height:1px;background:#888}
.t-text{top:34px;width:172px;font-size:6px;line-height:12px;color:#bbb}
.t-arrow{top:670px;width:20px;height:20px;border:1px solid #ccc;border-radius:50%}
.r-desc{left:140px;top:826px;width:394px;text-align:center;font-size:6.5px;font-style:italic;color:#aaa;line-height:11px}
.field{height:23px;border:1px solid var(--line);background:var(--field);font-size:6px;color:#888;padding:8px 9px}
.field.select::after{content:"";position:absolute;right:18px;top:0;height:100%;width:1px;background:var(--line)}
.caret{right:6px;top:10px;width:0;height:0;border-left:3px solid transparent;border-right:3px solid transparent;border-top:4px solid #bbb}
.btn{top:985px;height:23px;background:linear-gradient(#6a7076,#43484c);color:#fff;font-size:8.5px;font-weight:700;text-align:center;line-height:23px;border-radius:2px}
.partners{left:0;top:1024px;width:674px;height:69px;background:var(--logos);border-top:2px solid #e6e6e6}
.partner{top:1046px;height:24px;background:#d3d3d3;border-radius:3px}
.footer{left:0;top:1093px;width:674px;height:107px;background:var(--dark)}
.social{top:1109px;width:21px;height:21px;border-radius:50%;background:#fff}
.f-rule{left:73px;top:1143px;width:528px;height:1px;background:#3c3c3c}
.f-nav{left:0;top:1154px;width:674px;text-align:center;font-size:6px;color:#fff;text-transform:uppercase}
.f-nav span{margin:0 8px}
.copy{left:0;top:1177px;width:674px;text-align:center;font-size:8px;color:#555}
</style>
</head>
<body>
<header>
  <div class="abs header"></div>
  <div class="abs header-rule"></div>
  <div class="abs brand"><div class="brand-mark"></div><div class="brand-name">Runovexa</div></div>
  <nav class="abs nav">
    <a class="active" href="#">Home</a><a href="#">About Us</a><a href="#">Services</a><a href="#">Testimonials</a><a href="#">Reservation</a><a href="#">Contact Us</a>
  </nav>
</header>

<section>
  <div class="abs hero" role="img" aria-label="Photo of a dark coupe driving on a motorway, background blurred by motion"></div>
  <h1 class="abs hero-title">RUNOVEXA RENT A CAR</h1>
  <p class="abs hero-sub">Sed ut perspiciatis unde omnis iste natus error sit volup-quasi architecto beatae vitae dicta sunt explicabo.</p>
  <svg class="abs hero-arrow" style="left:76px" viewBox="0 0 18 18"><path d="M11 5 7 9l4 4" fill="none" stroke="#fff" stroke-width="1.3"/></svg>
  <svg class="abs hero-arrow" style="left:98px" viewBox="0 0 18 18"><path d="M7 5l4 4-4 4" fill="none" stroke="#fff" stroke-width="1.3"/></svg>
</section>

<section>
  <h2 class="abs sec-title" style="top:381px">Featured Service</h2>
  <div class="abs sec-rule" style="top:411px"></div>
  <div class="abs service" style="left:71px">
    <svg viewBox="0 0 34 34" fill="none" stroke="#888" stroke-width="1"><rect x="7" y="11" width="20" height="14"/><path d="M3 15v7M7 18H3M27 15h4v7h-4M13 11V8h8v3M18 14l-3 5h4l-3 5"/></svg>
    <div class="icon-base"></div><h3>Engine Installment</h3>
    <p>Quisque est enim lacinia lobortis da viverra interdum, quam. In sagittis, eros faucibus ullamcorper nibh dolor</p>
  </div>
  <div class="abs service" style="left:206px">
    <svg viewBox="0 0 34 34" fill="none" stroke="#888" stroke-width="1"><circle cx="17" cy="15" r="8"/><circle cx="17" cy="15" r="3"/><path d="M17 4v3M17 23v3M6 15h3M25 15h3M9 23l14-14M11 27l6-6"/></svg>
    <div class="icon-base"></div><h3>Car Maintainance</h3>
    <p>Quisque est enim lacinia lobortis da viverra interdum, quam. In sagittis, eros faucibus ullamcorper nibh dolor</p>
  </div>
  <div class="abs service" style="left:339px">
    <svg viewBox="0 0 34 34" fill="none" stroke="#888" stroke-width="1"><path d="M2 21v-4l6-1 5-5h10l6 5 3 1v4z"/><circle cx="9" cy="22" r="3"/><circle cx="25" cy="22" r="3"/></svg>
    <div class="icon-base"></div><h3>Vehicle Tuning</h3>
    <p>Quisque est enim lacinia lobortis da viverra interdum, quam. In sagittis, eros faucibus ullamcorper nibh dolor</p>
  </div>
  <div class="abs service" style="left:472px">
    <svg viewBox="0 0 34 34" fill="none" stroke="#888" stroke-width="1"><path d="M7 3h20M17 3v6M12 9h10M14 12l-2 3M17 12v3M20 12l2 3M9 30V24l3-4h10l3 4v6zM6 30h22"/></svg>
    <div class="icon-base"></div><h3>Clean &amp; Washing</h3>
    <p>Quisque est enim lacinia lobortis da viverra interdum, quam. In sagittis, eros faucibus ullamcorper nibh dolor</p>
  </div>
</section>

<section>
  <div class="abs testimonials" role="img" aria-label="Darkened photo of a sports car behind the testimonials"></div>
  <h2 class="abs sec-title t-title" style="top:565px">Testimonials</h2>
  <div class="abs sec-rule" style="top:594px;background:#777"></div>
  <p class="abs t-sub">Sed ut perspiciatis unde omnis iste natus error sit voluptatem accusantium doloremque laudantium, totam rem aperiam,</p>
  <div class="abs t-card" style="left:73px">
    <div class="abs t-photo" style="left:11px" role="img" aria-label="Portrait of a customer"></div>
    <div class="abs t-name" style="left:66px">Omar Hale , City Name</div>
    <div class="abs t-line" style="left:64px"></div>
    <p class="abs t-text" style="left:66px">“ vero eos et accusamus et iusto odio dignissimos ducimus qui blanditiis praesentium voluptatum deleniti atque corr upti quos dolores et quas molestias excepturi sint occaecati cupiditate non provident. ”</p>
  </div>
  <div class="abs t-card" style="left:349px">
    <div class="abs t-photo" style="right:11px;background:linear-gradient(#b9a79a,#3a3d44)" role="img" aria-label="Portrait of a customer"></div>
    <div class="abs t-name" style="right:66px">Omar Hale , City Name</div>
    <div class="abs t-line" style="left:5px"></div>
    <p class="abs t-text" style="left:8px;text-align:right">vero eos et accusamus et iusto odio dignissimos duc ” qui blanditiis praesentium voluptatum deleniti atque corr upti quos dolores et quas molestias excepturi sint occaecati “ cupiditate non provident.</p>
  </div>
  <svg class="abs t-arrow" style="left:41px" viewBox="0 0 20 20"><path d="M11.5 6 7.5 10l4 4" fill="none" stroke="#fff" stroke-width="1.3"/></svg>
  <svg class="abs t-arrow" style="left:610px" viewBox="0 0 20 20"><path d="M8.5 6l4 4-4 4" fill="none" stroke="#fff" stroke-width="1.3"/></svg>
</section>

<section>
  <h2 class="abs sec-title" style="top:783px">Reservation Form</h2>
  <div class="abs sec-rule" style="top:812px"></div>
  <p class="abs r-desc">Lorem ipsum dolor sit amet, consectetur adipisicing elit, sed do eiusmod tempor incididunt ut labore et dolore magna aliqua. Ut enim ad minim veniam, quis nostrud exercitation ullamco laboris nisi ut aliquip ex ea commodo consequat</p>
  <div class="abs field" style="left:74px;top:867px;width:169px">Name:</div>
  <div class="abs field" style="left:252px;top:867px;width:169px">Email:</div>
  <div class="abs field" style="left:430px;top:867px;width:169px;height:91px">Special Requests :</div>
  <div class="abs field" style="left:74px;top:902px;width:169px">Pick-up Date :</div>
  <div class="abs field select" style="left:252px;top:902px;width:169px">Pick-up Location :<span class="abs caret"></span></div>
  <div class="abs field" style="left:74px;top:935px;width:169px">Dorp off Date :</div>
  <div class="abs field select" style="left:252px;top:935px;width:169px">Passenger Information :<span class="abs caret"></span></div>
  <div class="abs btn" style="left:209px;width:125px">BOOK A RESERVATION</div>
  <div class="abs btn" style="left:341px;width:123px">CALL THE NUMBER</div>
</section>

<section>
  <div class="abs partners"></div>
  <div class="abs partner" style="left:77px;width:75px"></div>
  <div class="abs partner" style="left:176px;width:55px"></div>
  <div class="abs partner" style="left:253px;width:76px"></div>
  <div class="abs partner" style="left:342px;width:75px"></div>
  <div class="abs partner" style="left:447px;width:40px;height:32px;top:1042px"></div>
  <div class="abs partner" style="left:518px;width:75px"></div>
</section>

<footer>
  <div class="abs footer"></div>
  <div class="abs social" style="left:246px"></div>
  <div class="abs social" style="left:273px"></div>
  <div class="abs social" style="left:299px"></div>
  <div class="abs social" style="left:325px"></div>
  <div class="abs social" style="left:352px"></div>
  <div class="abs social" style="left:378px"></div>
  <div class="abs social" style="left:404px"></div>
  <div class="abs f-rule"></div>
  <div class="abs f-nav">
    <span>Home</span>|<span>About Us</span>|<span>Services</span>|<span>Credit Card Form</span>|<span>Our Fleet</span>|<span>Contact Us</span>
  </div>
  <div class="abs copy">Copyright© runovexarent.example,2015, All right Reserved.</div>
</footer>
</body>
</html>
```